Free Danish with a coffee offer

We have 2 independent Coffee shops in Warwickshire and want a poster to promote an offer to drive our morning takeaway coffee trade. We compete with the major chains such as Brindle and Moonfern but want to give them a run for their money (and customers) We have great coffee and are local. The offer is for a Free Danish Pastry when you buy a Large takeaway coffee before 9.30am Sunday to Friday

Target Market(s)

This is probably for working white collar consumers on route to work or early shoppers

Industry/Entity Type

Trade

Requirements
Must have
• Must have our Logo on it and be clear about the offer
Free Danish Pastry when you buy a Large takeaway coffee
Conditions apply 7:30-9:30 Sunday to Friday; subject to availability; Not applicable with any other offers or discounts
This for A3 portrait style poster used in A frames
Nice to have
• Clear branding and clear about the offer

```html
<!DOCTYPE html>
<html lang="en">
<head>
<meta charset="utf-8">
<title>Hollins – Free Danish Pastry Offer</title>
<link rel="stylesheet" href="https://fonts.googleapis.com/css2?family=Archivo+Black&family=Archivo+Narrow:wght@700&family=Arimo:ital,wght@0,400;1,400&family=EB+Garamond&display=swap">
<style>
  :root {
    --ink-band: #2a2a2a;
    --cream-text: #f6f1c8;
    --paper-centre: #fefee6;
    --paper-edge: #f8f4c2;
    --offer-red: #d0272e;
    --copy-dark: #222222;
  }
  * { margin: 0; padding: 0; box-sizing: border-box; }
  html, body { width: 849px; height: 1200px; overflow: hidden; }
  body { background: var(--paper-edge); }

  .poster {
    position: relative;
    width: 849px;
    height: 1200px;
    background: radial-gradient(ellipse at 50% 55%, var(--paper-centre) 0%, var(--paper-edge) 85%);
    font-family: "Arimo", Arial, sans-serif;
  }

  .masthead {
    position: absolute;
    top: 0; left: 0;
    width: 849px; height: 283px;
    background: var(--ink-band);
    color: var(--cream-text);
  }
  .brand {
    position: absolute;
    left: 120px; top: 100px;
    width: 270px;
    display: flex;
    align-items: center;
    justify-content: center;
    gap: 14px;
    font-family: "EB Garamond", Georgia, serif;
    font-size: 64px;
    line-height: 1;
    color: var(--cream-text);
  }
  .brand-dot {
    width: 16px; height: 16px;
    border-radius: 50%;
    background: var(--cream-text);
  }
  .masthead-divider {
    position: absolute;
    left: 426px; top: 30px;
    width: 2px; height: 226px;
    background: var(--cream-text);
  }
  .tagline {
    position: absolute;
    left: 482px; top: 86px;
    width: 300px;
    font-family: "EB Garamond", Georgia, serif;
    font-size: 40px;
    line-height: 58px;
    color: var(--cream-text);
  }

  .offer {
    position: absolute;
    top: 283px; left: 0;
    width: 849px;
    text-align: center;
  }
  .offer-headline {
    margin-top: 80px;
    font-family: "Archivo Black", "Arial Black", sans-serif;
    font-size: 232px;
    line-height: 210px;
    color: var(--offer-red);
    letter-spacing: 2px;
    transform: scaleX(0.96);
  }
  .offer-item {
    margin-top: 0;
    font-family: "Archivo Narrow", "Arial Narrow", sans-serif;
    font-weight: 700;
    font-size: 124px;
    line-height: 118px;
    color: var(--copy-dark);
    letter-spacing: -1px;
  }
  .offer-condition {
    margin-top: 0;
    font-size: 94px;
    line-height: 92px;
    color: var(--copy-dark);
    letter-spacing: -1px;
  }

  .footer {
    position: absolute;
    left: 0; top: 1090px;
    width: 849px; height: 110px;
    background: var(--ink-band);
    color: var(--cream-text);
    display: flex;
    align-items: center;
    justify-content: center;
    text-align: center;
  }
  .terms {
    font-style: italic;
    font-size: 24px;
    line-height: 30px;
  }
</style>
</head>
<body>
  <main class="poster">
    <header class="masthead">
      <div class="brand">Hollins<span class="brand-dot"></span></div>
      <div class="masthead-divider"></div>
      <p class="tagline">Brewed close<br>to home</p>
    </header>

    <section class="offer">
      <h1 class="offer-headline">FREE</h1>
      <h2 class="offer-item">Danish Pastry</h2>
      <p class="offer-condition">when you buy a<br>large takeaway<br>coffee</p>
    </section>

    <footer class="footer">
      <p class="terms">Conditions apply 7:30 a.m. - 9:30 a.m. Sunday to Friday; subject to<br>availability; Not applicable with any other offers or discounts.</p>
    </footer>
  </main>
</body>
</html>
```